Law Firm Banner Ads

Hi, I am an account manager for an Ad Agency that is looking for new Banner ads for a client of ours, The Brandt Law Firm. We would like new ads for their Display Campaigns. The Law Firm Specializes in Criminal Defense, DUIs and a bunch of other stuff. We would like the ads to either list a few key areas or focus on just one area, like DUIs. It is up to you guys on how you would like to do it, and we are open to either approach and simply planning on choosing the one that looks the best and looks like it has the most potential to drive traffic/conversions but we tend to get the best results from designers when we let them have as much freedom as possible. So feel free to make it however you like. We normally ask that the banners match the website because we've seen that congruency helps increase conversion rates, but in this case the website is getting re-made because it is so ugly. If you can match the look of site without making ugly ads, your chances of winning probably do increase, or maybe try to match the mobile site instead of the desktop stie. On the other hand, if you make ads that are super awesome/unique and don't look like the site, your chances of winning can increase as well.
Also feel free to use any text or call to action buttons that you think will look/perform the best. We tend to see that letting people know what they get, rather than what they have to do, tends to work the best.
We are looking for 300x600, 300x50, 300x250, 728x90. Only one size of your choice is required but make as many as you want to showcase the different features of your design.
Animated GIFs and static images are allowed but no Flash.
Size limit is 60kbs.
Some assets are provided but you might want to refer to the web, and desktop/mobile sites for other, more current assets. The ads included are their current ads which are live right now.
Updates
Hi Everybody,
Industry/Entity Type
Law Firm

```html
<!DOCTYPE html>
<html lang="en">
<head>
<meta charset="utf-8">
<title>The Brandt Law Firm – Banner 300x600</title>
<link rel="stylesheet" href="https://fonts.googleapis.com/css2?family=Open+Sans:wght@600;700&display=swap">
<style>
  :root {
    --maroon: #3d0000;
    --maroon-stripe: #4a0606;
    --gold: #b09a68;
    --gold-light: #cbb88a;
    --gold-dark: #7d6c45;
    --frame: #8f8472;
    --white: #ffffff;
    --band: #b3a27a;
    --band-text: #5a0000;
  }
  * { margin: 0; padding: 0; box-sizing: border-box; }
  html, body { width: 1200px; height: 2400px; overflow: hidden; }
  body {
    position: relative;
    background-color: var(--maroon);
    background-image: repeating-linear-gradient(135deg, var(--maroon) 0 14px, var(--maroon-stripe) 14px 17px);
    font-family: "Open Sans", Arial, sans-serif;
  }
  .building-art {
    position: absolute;
    left: 0; top: 71px;
    width: 1200px; height: 605px;
    background: linear-gradient(180deg, var(--gold-light) 0%, var(--gold) 55%, var(--gold-dark) 100%);
    opacity: 0.85;
  }
  .firm-name {
    position: absolute;
    top: 706px; left: 0; width: 1200px;
    text-align: center;
    font-family: "Open Sans", Arial, sans-serif;
    font-weight: 700;
    font-size: 84px;
    line-height: 1;
    color: var(--gold);
  }
  .rule {
    position: absolute; left: 0; width: 1200px; height: 11px;
    background: var(--white);
  }
  .rule--top { top: 864px; }
  .rule--bottom { top: 2078px; }
  .practice-list { position: absolute; top: 922px; left: 42px; list-style: none; }
  .practice {
    display: flex; align-items: center;
    height: 165px; margin-bottom: 72px;
  }
  .practice-icon {
    width: 165px; height: 165px;
    border: 8px solid var(--frame);
    display: flex; align-items: center; justify-content: center;
    flex-shrink: 0;
  }
  .practice-icon svg { width: 110px; height: 110px; }
  .practice-label {
    margin-left: 33px;
    font-weight: 600;
    font-size: 108px;
    line-height: 1;
    color: var(--white);
    white-space: nowrap;
    letter-spacing: -0.5px;
  }
  .contact-band {
    position: absolute; left: 0; top: 2098px;
    width: 1200px; height: 302px;
    background: var(--band);
  }
  .contact-phone, .contact-web {
    position: absolute; left: 0; width: 1200px;
    text-align: center;
    color: var(--band-text);
    line-height: 1.1;
    white-space: nowrap;
  }
  .contact-phone { top: 2135px; font-weight: 600; font-size: 98px; }
  .contact-web { top: 2266px; font-weight: 700; font-size: 70px; }
</style>
</head>
<body>
  <div class="building-art" role="img" aria-label="Gold classical courthouse with columns and pediment"></div>
  <h1 class="firm-name">The Brandt Law Firm</h1>
  <div class="rule rule--top"></div>

  <ul class="practice-list">
    <li class="practice">
      <span class="practice-icon">
        <svg viewBox="0 0 100 100" fill="var(--gold-light)"><path d="M8 32h80v14H48l-4 6h-8l-6 24H16l6-24h-8l-6-6z"/></svg>
      </span>
      <span class="practice-label">Criminal Defence</span>
    </li>
    <li class="practice">
      <span class="practice-icon">
        <svg viewBox="0 0 100 100" fill="none" stroke="var(--gold-light)" stroke-width="7"><circle cx="26" cy="60" r="17"/><circle cx="74" cy="60" r="17"/><path d="M38 42q12-14 24 0"/></svg>
      </span>
      <span class="practice-label">DUI Defense</span>
    </li>
    <li class="practice">
      <span class="practice-icon">
        <svg viewBox="0 0 100 100" fill="var(--gold-light)"><path d="M34 70V46a16 16 0 0 1 32 0v24z"/><rect x="26" y="72" width="48" height="10"/></svg>
      </span>
      <span class="practice-label">Appeals</span>
    </li>
    <li class="practice">
      <span class="practice-icon">
        <svg viewBox="0 0 100 100" fill="none" stroke="var(--gold-light)" stroke-width="6"><path d="M34 44V32a16 16 0 0 1 32 0v12"/><circle cx="50" cy="64" r="22"/><circle cx="50" cy="64" r="6" fill="var(--gold-light)"/></svg>
      </span>
      <span class="practice-label">White Collar</span>
    </li>
    <li class="practice">
      <span class="practice-icon">
        <svg viewBox="0 0 100 100" fill="none" stroke="var(--gold-light)" stroke-width="6"><path d="M50 12l32 10v24c0 22-14 36-32 44C32 82 18 68 18 46V22z"/><path d="M30 66L66 30" stroke-width="12"/></svg>
      </span>
      <span class="practice-label">Sex Crimes</span>
    </li>
  </ul>

  <div class="rule rule--bottom"></div>
  <footer class="contact-band"></footer>
  <p class="contact-phone">Call us at 480-555-0142</p>
  <p class="contact-web">www.TheBrandtLawFirm.com</p>
</body>
</html>
```